Modern business card for triathlon training business in Australia

We need a business card design for our triathlon training company.

Pace with Us Fitness is an Australian business, owned by women, run for women. Pace with Us Fitness helps women prepare or improve triathlon skills and confidence through triathlon camps completely designed for women.

Our camps focus on preparing women both physically and mentally for their next (or first!) triathlon.

You can see our website www.pacewithusfitness.com.au for more info about our business and our style.

We've attached two of our logos and are happy to consider a design that utilised either colour scheme with the teal colour being our 'feature' colour. We don't want overly feminine cards but rather cards that are professional and neat. If the inclusion of any pictures/art is warranted, this should be focused on our swim/ride/run theme and in that specific order (swim/ride/run).

The business card needs to be a printable design and the contact details will need to change for our two employees.

Target Market(s)

Female clients and partners/vendors/sponsors that we work with in the triathlon industry

Industry/Entity Type

Fitness

Contact Information for Business Card

Pace with Us Fitness (business name)
Nina Carver
Business Director
Mobile: 0438 916 207
Email: nina@pacewithusfitness.com.au
www.pacewithusfitness.com.au

Second business card:
Pace with Us Fitness
Bel Stray
Coaching Director
Mobile: 0459 260 718
Email: bel@pacewithusfitness.com.au

Font styles to use
Serif
Sans Serif

Requirements
Must have
• Core contact details above, our logo and be a printable design
Should not have
• Pink
• Cursive/script fonts

```html
<!DOCTYPE html>
<html lang="en">
<head>
<meta charset="utf-8">
<title>Pace with Us Fitness – Business Cards</title>
<link rel="stylesheet" href="https://fonts.googleapis.com/css2?family=Didact+Gothic&family=Questrial&display=swap">
<style>
  :root {
    --page-bg: #ecebe8;
    --teal-light: #00bdcf;
    --teal-dark: #00a0b2;
    --text-white: #ffffff;
    --card-shadow: rgba(0, 0, 0, 0.28);
  }
  * { margin: 0; padding: 0; box-sizing: border-box; }
  html, body {
    width: 1200px;
    height: 750px;
    overflow: hidden;
  }
  body {
    position: relative;
    background: var(--page-bg);
    font-family: "Questrial", "Didact Gothic", sans-serif;
    color: var(--text-white);
  }
  .business-card {
    position: absolute;
    width: 476px;
    height: 272px;
    background: var(--teal-light);
    overflow: hidden;
    box-shadow: 0 6px 18px var(--card-shadow);
  }
  .business-card--nina { left: 213px; top: 70px; }
  .business-card--bel  { left: 402px; top: 385px; }

  .card-shapes {
    position: absolute;
    inset: 0;
    width: 100%;
    height: 100%;
  }
  .card-shapes .arc { fill: var(--teal-dark); }

  .brand-name {
    position: absolute;
    left: 18px;
    top: 22px;
    width: 200px;
    font-family: "Didact Gothic", sans-serif;
    font-size: 34px;
    line-height: 38px;
    color: var(--text-white);
  }

  .person {
    position: absolute;
    left: 285px;
    top: 48px;
  }
  .person-name {
    font-size: 23px;
    letter-spacing: 0.3px;
    line-height: 28px;
    -webkit-text-stroke: 0.6px var(--text-white);
  }
  .person-role {
    font-size: 16px;
    line-height: 22px;
  }

  .contact-list {
    position: absolute;
    right: 8px;
    bottom: 8px;
    list-style: none;
    text-align: right;
    font-size: 15.5px;
    line-height: 20px;
  }
</style>
</head>
<body>

  <article class="business-card business-card--nina">
    <svg class="card-shapes" viewBox="0 0 476 272" aria-hidden="true">
      <circle class="arc" cx="640" cy="230" r="410"/>
      <circle class="arc" cx="-30" cy="330" r="190"/>
    </svg>
    <p class="brand-name">Pace with Us Fitness</p>
    <div class="person">
      <h2 class="person-name">Nina Carver</h2>
      <p class="person-role">Business Director</p>
    </div>
    <ul class="contact-list">
      <li>Mobile: 0438 916 207</li>
      <li>Email: nina@pacewithusfitness.com.au</li>
      <li>www.pacewithusfitness.com.au</li>
    </ul>
  </article>

  <article class="business-card business-card--bel">
    <svg class="card-shapes" viewBox="0 0 476 272" aria-hidden="true">
      <circle class="arc" cx="640" cy="230" r="410"/>
      <circle class="arc" cx="-30" cy="330" r="190"/>
    </svg>
    <p class="brand-name">Pace with Us Fitness</p>
    <div class="person">
      <h2 class="person-name">Bel Stray</h2>
      <p class="person-role">Coaching Director</p>
    </div>
    <ul class="contact-list">
      <li>Mobile: 0459 260 718</li>
      <li>Email: bel@pacewithusfitness.com.au</li>
      <li>www.pacewithusfitness.com.au</li>
    </ul>
  </article>

</body>
</html>
```